Domestic violence resource cards for distribution to at-risk patients in an emergency department

Using the attached image(or very similar) and text document, a tri-fold business card is requested that integrates the image on the outside and the document content throughout the card's remaining faces. A creative format is requested, one that does not look like the typical cold, uncaring bullet point outlines that are found in similar resource projects. Bold or larger font sizes are requested for headings and body text is not required to be aligned or justified and the bullet points in the supplied document can be removed for creative license. Palattes should be clear, avoiding neons or implied target gender. Legibility is paramount, but again a creative presentation of a very serious subject is our goal. These cards are intended to be distributed to patients or others in the emergency department that may benefit from domestic violence resources. The business card size is mandatory so that the card can be concealed if needed by the receiver.
Updates

Reason: There are several revisions from designers that we are anxiously awaiting; we want to provide time for these designers to submit new designs but also continue spending time with their families and friends around the holiday season.

Target Market(s)

Patients and family in contact with emergency services

Industry/Entity Type

Healthcare

Contact Information for Business Card

Double sided tri-fold card with image on outer sides, text content and resource phone numbers on the exterior. When complete, the card should fold to standard US business card size.

Font styles to use
Other font styles liked:
• Designer's choice, but clear and legible

Requirements
Must have
• See above description. Card must be tri-fold, fold down to standard business card size, remain easily readable, and fold along the long edge.
Should not have
• Cartoon images; bloated fonts or clipart; bright, flashy neon or rainbow-like colors; additional graphics or charts.

```html
<!DOCTYPE html>
<html lang="en">
<head>
<meta charset="utf-8">
<title>You Are Not Alone – Resource Card</title>
<link href="https://fonts.googleapis.com/css2?family=Montserrat:wght@700;800&family=Open+Sans:wght@400;700&display=swap" rel="stylesheet">
<style>
  :root {
    --plum: #6a2262;
    --ink: #111111;
    --paper: #ffffff;
    --text: #1a1a1a;
    --photo-dark: #0b0b0b;
    --photo-mid: #5a5a5a;
    --photo-light: #cfcfcf;
  }
  * { box-sizing: border-box; margin: 0; padding: 0; }
  html, body { width: 720px; height: 1200px; overflow: hidden; background: var(--paper); }
  body { font-family: "Open Sans", Arial, sans-serif; color: var(--text); }
  .card { position: relative; width: 720px; height: 1200px; }

  .cover { position: absolute; left: 0; top: 0; width: 720px; height: 468px; background: var(--photo-dark); overflow: hidden; }
  .cover-photo {
    position: absolute; right: 0; top: 0; width: 440px; height: 468px;
    background: radial-gradient(ellipse at 60% 55%, var(--photo-light) 0%, var(--photo-mid) 38%, var(--photo-dark) 75%);
  }
  .cover-title {
    position: absolute; left: 34px; top: 36px; width: 280px;
    transform: rotate(180deg);
    font-family: "Montserrat", Arial, sans-serif; font-weight: 800;
    color: var(--paper); font-size: 66px; line-height: 1.38; text-align: right;
    white-space: nowrap;
  }

  .band { background: var(--plum); color: var(--paper); }
  .contacts-band { position: absolute; left: 0; top: 468px; width: 720px; height: 80px; padding: 16px 50px; }
  .contacts-band h2 { font-family: "Montserrat", Arial, sans-serif; font-weight: 700; font-size: 36px; letter-spacing: 1px; }

  .contacts { position: absolute; left: 0; top: 560px; width: 720px; padding: 0 40px 0 50px; display: grid; grid-template-columns: 300px 1fr; column-gap: 36px; }
  .contact { margin-bottom: 20px; font-size: 17px; line-height: 1.25; }
  .contact-name { font-weight: 700; }

  .questions { position: absolute; left: 0; top: 850px; width: 720px; height: 350px; transform: rotate(180deg); }
  .questions-band { height: 80px; padding: 20px 50px; }
  .questions-band h2 { font-family: "Montserrat", Arial, sans-serif; font-weight: 700; font-size: 32px; letter-spacing: 1.5px; }
  .question-list { display: grid; grid-template-columns: 1fr 1fr; column-gap: 30px; padding: 18px 40px 0 50px; height: 212px; }
  .question-list ul { list-style: none; }
  .question-list li { font-size: 16px; line-height: 1.25; margin-bottom: 6px; }
  .question-list li::before { content: "- "; }
  .warning { border-top: 3px solid var(--plum); margin: 0 40px; padding-top: 8px; font-weight: 700; color: var(--plum); font-size: 20px; font-style: italic; }
</style>
</head>
<body>
<div class="card">
  <section class="cover">
    <div class="cover-photo" role="img" aria-label="Black and white photograph of two wrists bound together with rope"></div>
    <h1 class="cover-title">YOU<br>ARE<br>NOT<br>ALONE</h1>
  </section>

  <header class="band contacts-band"><h2>CONTACTS</h2></header>

  <section class="contacts">
    <div class="contacts-col">
      <p class="contact"><span class="contact-name">Harbor Line Support Hotline</span><br>1-800-555-0142</p>
      <p class="contact"><span class="contact-name">www.safeharborlist.org</span></p>
      <p class="contact"><span class="contact-name">Safe Haven Metro: Domestic Violence Crisis Resource</span><br>303-555-0118</p>
      <p class="contact"><span class="contact-name">Northgate Domestic Violence Resources</span><br>303-555-0163</p>
    </div>
    <div class="contacts-col">
      <p class="contact"><span class="contact-name">The Lighthouse Center</span><br>1-888-555-0127</p>
      <p class="contact"><span class="contact-name">Oak Branch Violence Resources</span><br>303-555-0175</p>
      <p class="contact"><span class="contact-name">Quiet Harbor: Sexual Assault Victim's Advocate</span><br>303-555-0190</p>
      <p class="contact"><span class="contact-name">Respect Matters: Teen Dating Resource</span> 1-866-555-0134 or text "respect" to 55500</p>
    </div>
  </section>

  <section class="questions">
    <header class="band questions-band"><h2>Does your partner ever...</h2></header>
    <div class="question-list">
      <ul>
        <li>Hit, kick, push, choke or slap you?</li>
        <li>Intimidate you with weapons or harmful objects?</li>
        <li>Force you to engage in sexual acts?</li>
        <li>Threaten to hurt you, your children or your friends/family?</li>
        <li>Threaten to deport you or tell others your personal information?</li>
      </ul>
      <ul>
        <li>Control where you go, who you talk to or who your friends are?</li>
        <li>Keep, hide or destroy your most important things?</li>
        <li>Blame, embarrass, or criticize you, make you feel worthless or guilty?</li>
        <li>Control your food, money, medicines or medical care?</li>
      </ul>
    </div>
    <p class="warning">You may be a victim of abuse or neglect!</p>
  </section>
</div>
</body>
</html>
```